Post card for annual skin cancer screening exam

We are looking to design a modern, classy, clean, but fun postcard that we will send out to patients to remind them to schedule their follow up exams for our dermatology office.

It should include our logo
http://tovimek.com/design/logo/jpg/tovimek2.jpg
http://tovimek.com/design/logo/jpg/tovimek.jpg

Address
Phone number
website

We are open to your ideas on wording, as something clever is always appreciated - though this is going to both young and elderly patients - so the message must be easy to read and clear.
Updates

Font styles to use
Serif

Colors
85cae6
3176b5

Requirements
Must have
• Logo
• Office address
• Phone number
• website
• call to action message - to schedule a follow up visit

```html
<!DOCTYPE html>
<html lang="en">
<head>
<meta charset="utf-8">
<title>Tovimek Dermatology – Skin Exam Reminder Postcard</title>
<link href="https://fonts.googleapis.com/css2?family=Arimo:wght@400;700&display=swap" rel="stylesheet">
<style>
  :root {
    --sky: #85cae6;
    --brand-blue: #3176b5;
    --navy: #1d3f6e;
    --teal: #2a8fb8;
    --sand: #e9dcc6;
    --paper: #ffffff;
    --mist: #e6f3fa;
    --ink: #23456f;
  }
  * { box-sizing: border-box; margin: 0; padding: 0; }
  html, body { width: 795px; height: 1200px; overflow: hidden; background: var(--paper); }
  body { position: relative; font-family: "Arimo", Arial, sans-serif; color: var(--ink); }

  .card {
    position: absolute; left: 40px; width: 715px; overflow: hidden;
    box-shadow: 3px 4px 10px rgba(0,0,0,0.35);
  }
  .card--front { top: 30px; height: 546px; }
  .card--back  { top: 612px; height: 540px; background: var(--paper); }

  .beach-photo {
    position: absolute; inset: 0;
    background:
      linear-gradient(90deg, rgba(255,255,255,0) 55%, rgba(238,214,190,0.85) 68%, rgba(245,228,210,0.9) 100%),
      linear-gradient(180deg, #a9d7ee 0%, #4f9fcf 14%, #3b8fc4 26%, #8cc8e2 40%, #d7e8ea 55%, var(--sand) 100%);
  }

  .front-copy { position: absolute; left: 74px; top: 78px; }
  .headline { font-weight: 700; font-size: 23px; line-height: 29px; text-transform: uppercase; }
  .headline__lead { color: var(--teal); }
  .headline__main { color: var(--navy); }
  .cta { margin-top: 16px; font-weight: 700; font-size: 17px; line-height: 24px; color: var(--brand-blue); text-transform: uppercase; }

  .brand { display: flex; align-items: center; gap: 10px; }
  .brand__dot { width: 26px; height: 26px; border-radius: 50%; background: var(--sky); flex: none; }
  .brand__name { font-weight: 700; font-size: 26px; color: var(--brand-blue); letter-spacing: 0.5px; }
  .card--front .brand { position: absolute; left: 74px; top: 255px; }
  .card--back .brand { position: absolute; left: 40px; top: 230px; }

  .contact { position: absolute; list-style: none; }
  .contact li { display: flex; align-items: center; gap: 10px; font-weight: 700; color: var(--navy); }
  .contact svg { width: 18px; height: 18px; flex: none; fill: var(--navy); }
  .card--front .contact { left: 86px; top: 396px; }
  .card--front .contact li { font-size: 16px; line-height: 27px; }
  .card--back .contact { left: 40px; top: 335px; }
  .card--back .contact li { font-size: 16px; line-height: 22px; margin-bottom: 20px; }
  .contact .address { align-items: flex-start; }

  .back-wash { position: absolute; inset: 0; width: 100%; height: 100%; }
  .back-copy { position: absolute; left: 29px; top: 40px; width: 330px; font-size: 15.5px; line-height: 20px; color: var(--brand-blue); }
  .back-copy p + p { margin-top: 20px; }
  .back-copy strong { font-weight: 700; }
</style>
</head>
<body>

<section class="card card--front">
  <div class="beach-photo" role="img" aria-label="Photo of a woman in a white sun hat on a sunny beach, a sunscreen drawing on her shoulder, sea and sailboat behind her"></div>

  <div class="front-copy">
    <h1 class="headline">
      <span class="headline__lead">It is time to schedule</span><br>
      <span class="headline__main">Your full body skin exam.</span>
    </h1>
    <p class="cta">Make an appointment today ~<br>online or by phone!</p>
  </div>

  <div class="brand">
    <span class="brand__dot"></span>
    <span class="brand__name">tovimek dermatology</span>
  </div>

  <ul class="contact">
    <li>
      <svg viewBox="0 0 24 24" aria-hidden="true"><path d="M12 2a10 10 0 1 0 0 20 10 10 0 0 0 0-20zm6.9 6h-3a15 15 0 0 0-1.3-3.9A8 8 0 0 1 18.9 8zM12 4c.8 1.2 1.5 2.5 1.9 4h-3.8c.4-1.5 1.1-2.8 1.9-4zM4.3 14a8 8 0 0 1 0-4h3.4a16 16 0 0 0 0 4zm.8 2h3a15 15 0 0 0 1.3 3.9A8 8 0 0 1 5.1 16zm3-8h-3a8 8 0 0 1 4.3-3.9A15 15 0 0 0 8.1 8zM12 20c-.8-1.2-1.5-2.5-1.9-4h3.8c-.4 1.5-1.1 2.8-1.9 4zm2.3-6H9.7a14 14 0 0 1 0-4h4.6a14 14 0 0 1 0 4zm.3 5.9a15 15 0 0 0 1.3-3.9h3a8 8 0 0 1-4.3 3.9zm1.7-5.9a16 16 0 0 0 0-4h3.4a8 8 0 0 1 0 4z"/></svg>
      WWW.TOVIMEK.COM
    </li>
    <li>
      <svg viewBox="0 0 24 24" aria-hidden="true"><path d="M6.6 10.8a15.1 15.1 0 0 0 6.6 6.6l2.2-2.2a1 1 0 0 1 1-.25 11.4 11.4 0 0 0 3.6.57 1 1 0 0 1 1 1V20a1 1 0 0 1-1 1A17 17 0 0 1 3 4a1 1 0 0 1 1-1h3.5a1 1 0 0 1 1 1c0 1.25.2 2.45.57 3.57a1 1 0 0 1-.25 1z"/></svg>
      (631) 555-7546 (SKIN)
    </li>
  </ul>
</section>

<section class="card card--back">
  <svg class="back-wash" viewBox="0 0 715 540" preserveAspectRatio="none" aria-hidden="true">
    <defs>
      <linearGradient id="wash" x1="0" y1="0" x2="0" y2="1">
        <stop offset="0" stop-color="#ffffff"/>
        <stop offset="0.45" stop-color="#d9eef8"/>
        <stop offset="1" stop-color="#bfe2f2"/>
      </linearGradient>
      <linearGradient id="swoosh" x1="0" y1="0" x2="1" y2="0">
        <stop offset="0" stop-color="#3176b5"/>
        <stop offset="1" stop-color="#85cae6"/>
      </linearGradient>
    </defs>
    <rect width="715" height="540" fill="url(#wash)"/>
    <path d="M300 0 C420 80 420 360 320 540 L715 540 L715 0 Z" fill="url(#swoosh)"/>
    <path d="M330 0 C440 90 440 360 345 540 L715 540 L715 0 Z" fill="#ffffff"/>
  </svg>

  <div class="back-copy">
    <p>For your convenience, we are<br>open six days a week with evening<br>and weekend hours.</p>
    <p>To request an appointment,<br>call us: <strong>(631) 555-7546 (SKIN)</strong> or use<br>our on-line appointment request form.</p>
  </div>

  <div class="brand">
    <span class="brand__dot"></span>
    <span class="brand__name">tovimek dermatology</span>
  </div>

  <ul class="contact">
    <li>
      <svg viewBox="0 0 24 24" aria-hidden="true"><path d="M12 2a10 10 0 1 0 0 20 10 10 0 0 0 0-20zm6.9 6h-3a15 15 0 0 0-1.3-3.9A8 8 0 0 1 18.9 8zM12 4c.8 1.2 1.5 2.5 1.9 4h-3.8c.4-1.5 1.1-2.8 1.9-4zM4.3 14a8 8 0 0 1 0-4h3.4a16 16 0 0 0 0 4zm.8 2h3a15 15 0 0 0 1.3 3.9A8 8 0 0 1 5.1 16zm3-8h-3a8 8 0 0 1 4.3-3.9A15 15 0 0 0 8.1 8zM12 20c-.8-1.2-1.5-2.5-1.9-4h3.8c-.4 1.5-1.1 2.8-1.9 4zm2.3-6H9.7a14 14 0 0 1 0-4h4.6a14 14 0 0 1 0 4zm.3 5.9a15 15 0 0 0 1.3-3.9h3a8 8 0 0 1-4.3 3.9zm1.7-5.9a16 16 0 0 0 0-4h3.4a8 8 0 0 1 0 4z"/></svg>
      WWW.TOVIMEK.COM
    </li>
    <li>
      <svg viewBox="0 0 24 24" aria-hidden="true"><path d="M6.6 10.8a15.1 15.1 0 0 0 6.6 6.6l2.2-2.2a1 1 0 0 1 1-.25 11.4 11.4 0 0 0 3.6.57 1 1 0 0 1 1 1V20a1 1 0 0 1-1 1A17 17 0 0 1 3 4a1 1 0 0 1 1-1h3.5a1 1 0 0 1 1 1c0 1.25.2 2.45.57 3.57a1 1 0 0 1-.25 1z"/></svg>
      (631) 555-7546 (SKIN)
    </li>
    <li class="address">
      <svg viewBox="0 0 24 24" aria-hidden="true"><path d="M12 2a7 7 0 0 0-7 7c0 5.2 7 13 7 13s7-7.8 7-13a7 7 0 0 0-7-7zm0 9.5a2.5 2.5 0 1 1 0-5 2.5 2.5 0 0 1 0 5z"/></svg>
      <span>240 Harbor Point Rd<br>Westbury NY 11590</span>
    </li>
  </ul>
</section>

</body>
</html>
```